New SKINCARE Label Design Project

Check out our website www.morlenbloom.com. We offer a few products that are all natural, from drinks to skincare. We have new packaging for the "Dewhaven Balm" and need a new label design. We'd like out of the box thinking, but it should fit the existing concept. The product label should contain cool words, can be creative and should contain ingredients as this is a regulation.

I have added some examples of what we’d like. Please base your design on this.

Target Market(s)

skincare, cosmetics, natural, cool, young

Industry/Entity Type

Skin Care Product

Requirements
Must have
• Label must fit the existing concept, but should be out of the box, potentially using unexpected colors... Clean design, clean fonts, very professional, but playful at the same time, can maybe include cartoons, stars,...
Nice to have
• Out of the box thinking, we'd like to stand out from all other brands by label design, it should catch the eye and interest people to buy our product.

```html
<!DOCTYPE html>
<html lang="en">
<head>
<meta charset="utf-8">
<title>Dewhaven Balm – Label Sheet</title>
<link href="https://fonts.googleapis.com/css2?family=Roboto+Condensed:wght@400;700&family=Roboto:wght@400&family=Raleway:wght@300;400&family=Caveat:wght@700&family=Indie+Flower&display=swap" rel="stylesheet">
<style>
  :root {
    --ink: #1a1a1a;
    --text: #333333;
    --grey: #9a9a9a;
    --frame: #3a3a3a;
    --lilac: #d8b6d6;
    --lilac-deep: #a98bc3;
    --butter: #efdf9a;
    --butter-band: #f3d089;
    --gold: #d8b46a;
    --steel: #5b86b3;
    --paper: #ffffff;
  }
  * { box-sizing: border-box; margin: 0; padding: 0; }
  html, body { width: 971px; height: 1200px; overflow: hidden; background: var(--paper); }
  .sheet { position: relative; width: 971px; height: 1200px; font-family: "Roboto", Arial, sans-serif; color: var(--text); }
  .sheet-frame { position: absolute; left: 27px; top: 3px; width: 894px; height: 1185px; border: 1.5px solid var(--frame); }

  .dimension { position: absolute; color: var(--grey); font-family: "Roboto", Arial, sans-serif; font-size: 30px; }
  .dimension--width { top: 1148px; width: 160px; text-align: center; }
  .dimension--height { left: 858px; top: 560px; transform: rotate(-90deg); transform-origin: center; width: 120px; text-align: center; }

  .label { position: absolute; top: 57px; width: 342px; height: 1066px; border: 1.2px solid var(--ink); background: var(--paper); }
  .label--her { left: 63px; }
  .label--him { left: 515px; }

  .brand-mark { position: absolute; display: flex; align-items: center; gap: 6px; color: var(--ink); font-family: "Raleway", sans-serif; font-weight: 400; }
  .brand-mark__dot { border-radius: 50%; background: var(--ink); flex: none; }
  .brand-mark--large { left: 36px; top: 126px; font-size: 34px; }
  .brand-mark--large .brand-mark__dot { width: 14px; height: 14px; }
  .brand-mark--small { left: 232px; top: 84px; font-size: 18px; }
  .brand-mark--small .brand-mark__dot { width: 8px; height: 8px; }

  .product-badge { position: absolute; left: 17px; top: 228px; width: 160px; height: 160px; border-radius: 50%; display: flex; flex-direction: column; align-items: center; justify-content: center; font-family: "Raleway", sans-serif; font-weight: 300; color: #2b2b2b; line-height: 0.95; }
  .label--her .product-badge { background: var(--lilac); }
  .label--him .product-badge { background: var(--butter); }
  .product-badge__name { font-size: 29px; letter-spacing: -0.5px; }
  .product-badge__type { font-size: 28px; margin-top: 2px; }

  .figure-slot { position: absolute; }
  .label--her .figure-slot { left: 50px; top: 398px; width: 92px; height: 262px; background: linear-gradient(180deg, #f1d7e3 0%, #b9a3d8 45%, #9c86c9 100%); }
  .label--him .figure-slot { left: 62px; top: 403px; width: 78px; height: 262px; background: linear-gradient(180deg, #9b7b64 0%, #a58ac9 35%, #c9c6a6 75%, #e6e3dc 100%); }

  .tagline { position: absolute; left: 0; width: 195px; text-align: center; color: #555; line-height: 1; }
  .label--her .tagline { top: 672px; }
  .label--him .tagline { top: 680px; }
  .tagline__start { display: block; font-family: "Caveat", cursive; font-size: 34px; color: var(--lilac-deep); }
  .tagline__line { display: block; font-family: "Roboto", sans-serif; font-size: 19px; }
  .tagline__word { display: block; font-family: "Indie Flower", cursive; font-size: 38px; letter-spacing: 2px; margin-top: 2px; }
  .label--her .tagline__word { color: var(--steel); }
  .label--him .tagline__word { color: var(--gold); }

  .benefits { position: absolute; left: 0; width: 195px; list-style: none; text-align: center; font-size: 10px; line-height: 13px; color: var(--ink); }
  .label--her .benefits { top: 796px; }
  .label--him .benefits { top: 790px; }
  .benefits li::before { content: "✦ "; }

  .claim-band { position: absolute; left: 12px; top: 861px; width: 171px; height: 37px; display: flex; align-items: center; justify-content: center; text-align: center; font-size: 13px; line-height: 15px; }
  .label--her .claim-band { background: var(--steel); color: #fff; }
  .label--him .claim-band { background: var(--butter-band); color: #333; }

  .promises { position: absolute; left: 38px; top: 907px; width: 110px; list-style: none; text-align: center; font-size: 10px; line-height: 12px; color: var(--ink); }
  .promises li { padding: 2px 0 3px; border-bottom: 1px dotted #999; }
  .promises li:last-child { border-bottom: none; }

  .volume { position: absolute; left: 0; width: 195px; top: 1011px; text-align: center; font-size: 12px; color: var(--ink); }

  .info { position: absolute; left: 208px; top: 135px; width: 122px; font-family: "Roboto Condensed", sans-serif; font-size: 10.3px; line-height: 14.1px; color: var(--ink); text-align: justify; }
  .info p { margin-bottom: 14px; }
  .info strong { font-weight: 700; }
  .info__steps span { display: block; }
  .info__story { position: absolute; left: 208px; width: 122px; top: 719px; font-family: "Roboto Condensed", sans-serif; font-size: 10.3px; line-height: 16px; color: var(--ink); text-align: justify; }
</style>
</head>
<body>
<main class="sheet">
  <div class="sheet-frame"></div>

  <!-- Label: her edition -->
  <section class="label label--her">
    <div class="brand-mark brand-mark--large"><span class="brand-mark__dot"></span>morlen</div>
    <div class="brand-mark brand-mark--small"><span class="brand-mark__dot"></span>morlen</div>
    <div class="product-badge"><span class="product-badge__name">DEWHAVEN</span><span class="product-badge__type">BALM</span></div>
    <div class="figure-slot" role="img" aria-label="Fashion illustration of a woman in a lilac suit and pink beret holding a pink bag"></div>
    <div class="tagline">
      <span class="tagline__start">Start</span>
      <span class="tagline__line">your day</span>
      <span class="tagline__line">with a</span>
      <span class="tagline__word">GLOW</span>
    </div>
    <ul class="benefits">
      <li>Perfect Illuminating</li>
      <li>Intense Hydration</li>
      <li>Imperfections fade</li>
      <li>Radiate from the inside</li>
    </ul>
    <div class="claim-band">Naturally nourishing<br>herbal extracts</div>
    <ul class="promises">
      <li>Nourishes and protects the skin.</li>
      <li>Skin feels chill again .</li>
      <li>Slows the aging of the skin.</li>
    </ul>
    <div class="volume">5fl oz/148ml</div>
    <div class="info">
      <p><strong>Ingredients/ingrediënten</strong> : Aqua, Glyceryl Stearate SE, Cetearyl Ethylhexanoate, Glycerin, Cetyl Alcohol, Propanediol, Isopropyl Myristate, Caledula Officinalis Flower Oil, Carica Papaya Seed Oil, Glyeryl Stearate, Rubus Idaeus Seed Oil, Dimethicone, Sodium PCA, Sodium Lactate, Fragrance, Alcohol, Bisabolol, Polyglyceryl-6, Palmitate / Succinate, Cetearyl Alcohol, Tetrasodium Glutamate Diacetate, Calendula Officinalis, Hypericum Perforatum, Urtica Urens, Fructose, Glycine, Niacinamide, Urea, Sodium, Hydroxide.</p>
      <p class="info__steps">Comments:<br>
        <strong>Step1:</strong> Clean your skin. <strong>Step 2:</strong> Use Dewhaven Balm for instant illumination. <strong>Step3:</strong> Put on your glamorous make-up. <strong>Stap1:</strong> reinig je gezicht. <strong>Stap2:</strong> gebruik Dewhaven Balm voor een onmiddelijke glow. <strong>Stap3:</strong> breng je glamorous make-up aan.</p>
      <p>also for sensitive skin/ook voor de gevoelige huid</p>
    </div>
    <p class="info__story">A good dose of herbal extracts including Calendula, Urtica and Hypericum will feed a tired skin, give it a healthy glow and give a balanced protection./Een goede dosis van kruidenextracten inclusief Calendula, Urtica en Hypericum zal de vermoeide huid voeden, geeft de huid een gezonde gloed en een gebalanceerde bescherming.</p>
  </section>

  <!-- Label: his edition -->
  <section class="label label--him">
    <div class="brand-mark brand-mark--large"><span class="brand-mark__dot"></span>morlen</div>
    <div class="brand-mark brand-mark--small"><span class="brand-mark__dot"></span>morlen</div>
    <div class="product-badge"><span class="product-badge__name">DEWHAVEN</span><span class="product-badge__type">BALM</span></div>
    <div class="figure-slot" role="img" aria-label="Fashion illustration of a young man in a purple sweater and khaki trousers"></div>
    <div class="tagline">
      <span class="tagline__start">Start</span>
      <span class="tagline__line">Looking</span>
      <span class="tagline__word">SMART</span>
    </div>
    <ul class="benefits">
      <li>Protect against dry skin</li>
      <li>Maximum Hydrator</li>
      <li>Skin feels chill</li>
      <li>Against redness</li>
    </ul>
    <div class="claim-band">Naturally nourishing<br>herbal extracts</div>
    <ul class="promises">
      <li>Nourishes and protects the skin.</li>
      <li>Skin feels chill again .</li>
      <li>Slows skin aging</li>
    </ul>
    <div class="volume">5fl oz/148ml</div>
    <div class="info">
      <p><strong>Ingredients/ingrediënten</strong> : Aqua, Glyceryl Stearate SE, Cetearyl Ethylhexanoate, Glycerin, Cetyl Alcohol, Propanediol, Isopropyl Myristate, Caledula Officinalis Flower Oil, Carica Papaya Seed Oil, Glyeryl Stearate, Rubus Idaeus Seed Oil, Dimethicone, Sodium PCA, Sodium Lactate, Fragrance, Alcohol, Bisabolol, Polyglyceryl-6, Palmitate / Succinate, Cetearyl Alcohol, Tetrasodium Glutamate Diacetate, Calendula Officinalis, Hypericum Perforatum, Urtica Urens, Fructose, Glycine, Niacinamide, Urea, Sodium, Hydroxide.</p>
      <p class="info__steps">Comments:<br>
        <strong>Step1:</strong> Clean your skin. <strong>Step 2:</strong> Use Dewhaven Balm for instant illumination. <strong>Stap1:</strong> reinig je gezicht. <strong>Stap2:</strong> gebruik Dewhaven Balm voor een onmiddelijke glow.</p>
      <p style="margin-top:28px">also for sensitive skin/ook voor de gevoelige huid</p>
    </div>
    <p class="info__story">A good dose of herbal extracts including Calendula, Urtica and Hypericum will feed a tired skin, give it a healthy glow and give a balanced protection./Een goede dosis van kruidenextracten inclusief Calendula, Urtica en Hypericum zal de vermoeide huid voeden, geeft de huid een gezonde gloed en een gebalanceerde bescherming.</p>
  </section>

  <div class="dimension dimension--width" style="left:164px">40mm</div>
  <div class="dimension dimension--width" style="left:616px">40mm</div>
  <div class="dimension dimension--height">125mm</div>
</main>
</body>
</html>
```